Website Design for Amberfold Vista Group – Professional, Modern, and Sustainable Energy Consulting

Amberfold Vista Group is a leading consultancy specializing in sustainable energy solutions. We are seeking a professional and visually appealing Squarespace website design to showcase our expertise and services. The website should reflect our brand identity, as defined by our new logo, and provide an engaging user experience. Please read carefully the attached document "Website product requirement rev 1.pdf".

```html
<!DOCTYPE html>
<html lang="en">
<head>
<meta charset="utf-8">
<title>Amberfold Vista Group – Sustainable Energy Consulting</title>
<link href="https://fonts.googleapis.com/css2?family=DM+Serif+Display&family=Libre+Caslon+Display&family=Work+Sans:ital,wght@0,400;0,500;0,600;0,700;1,400;1,600&display=swap" rel="stylesheet">
<style>
:root{
  --olive:#3a3d24;
  --cream:#f8f4ea;
  --ink:#1a1a1a;
  --navy:#24324a;
  --green:#2fae5a;
  --white:#ffffff;
  --muted:#555555;
}
*{margin:0;padding:0;box-sizing:border-box}
html,body{width:1200px;height:3976px;overflow:hidden;background:var(--white)}
body{font-family:"Work Sans",sans-serif;color:var(--ink);position:relative}
.block{position:absolute;left:0;width:1200px}
.site-header{top:0;height:93px;background:var(--white)}
.brand{position:absolute;left:56px;top:34px;display:flex;align-items:center;gap:10px;font-family:"Work Sans",sans-serif;font-weight:600;font-size:19px;color:var(--navy)}
.brand-dot{width:28px;height:28px;border-radius:50%;background:var(--green)}
.main-nav{position:absolute;right:70px;top:48px;display:flex;gap:14px;font-size:12px;color:#333}
.hero{top:93px;height:450px;background:linear-gradient(180deg,#4a5a74 0%,#26344a 45%,#1b2433 100%);text-align:center;color:var(--white)}
.hero h1{font-family:"DM Serif Display",serif;font-weight:400;font-size:59px;line-height:70px;margin-top:58px;letter-spacing:-1px}
.hero p{font-size:16px;line-height:28px;margin:22px auto 0;width:740px}
.btn{display:inline-flex;align-items:center;justify-content:center;font-size:11px;letter-spacing:2px;font-weight:500}
.btn-light{background:var(--cream);color:var(--ink)}
.hero .btn{position:absolute;left:467px;top:313px;width:268px;height:57px}
.vision{top:543px;height:162px;background:var(--olive);color:var(--white);text-align:center;font-family:"Libre Caslon Display",serif;font-size:22px;line-height:32px;padding:42px 150px 0}
.about{top:705px;height:442px;background:var(--white)}
.about h2,.services h2{font-family:"Libre Caslon Display",serif;font-weight:400;font-size:76px;letter-spacing:-1px}
.about h2{position:absolute;left:50px;top:72px}
.about p{position:absolute;left:51px;top:180px;width:360px;font-size:15.5px;line-height:28px;color:#333}
.btn-dark{background:#000;color:var(--white)}
.about .btn{position:absolute;left:51px;top:367px;width:176px;height:56px}
.photo{position:absolute}
.services{top:1147px;height:635px;background:var(--olive);color:var(--white)}
.services h2{position:absolute;left:606px;top:20px;font-size:74px}
.service-list{position:absolute;left:674px;top:154px;width:480px;font-size:11.5px;line-height:19px;list-style:none;counter-reset:s}
.service-list li{counter-increment:s;margin-bottom:12px;position:relative;padding-left:12px}
.service-list li::before{content:counter(s)".";position:absolute;left:-2px}
.service-list strong{font-weight:700;display:block}
.service-list em{font-style:italic;opacity:.9}
.services .btn{position:absolute;left:699px;top:462px;width:221px;height:57px}
.stories{top:1782px;height:270px;text-align:center}
.stories h2,.commit h2{font-family:"Libre Caslon Display",serif;font-weight:400;font-size:58px;color:var(--navy);letter-spacing:-1px}
.stories h2{margin-top:42px}
.stories blockquote{color:var(--green);font-style:italic;font-weight:600;font-size:13.5px;line-height:24px;width:820px;margin:18px auto 0}
.stories cite{display:block;margin-top:14px;font-size:13px;font-weight:600;font-style:italic;color:#222}
.mosaic{height:247px}
.commit{top:2299px;height:198px;text-align:center}
.commit h2{margin-top:40px;font-size:60px}
.commit p{margin-top:18px;color:var(--green);font-weight:600;font-size:17px}
.site-footer{top:3618px;height:358px;background:var(--cream)}
.footer-tag{position:absolute;left:100px;top:52px;width:520px;font-size:13.5px;line-height:24px;color:#333}
.footer-links{position:absolute;left:124px;top:116px;list-style:disc;font-size:13px;font-weight:600;line-height:31px}
.social{position:absolute;left:100px;top:269px;display:flex;gap:13px}
.social span{width:24px;height:24px;background:#000}
.signup-label{position:absolute;left:748px;top:54px;font-size:12.5px;color:#333}
.email{position:absolute;left:748px;top:87px;width:309px;height:55px;background:var(--white);border:1px solid #e8e3d8;font-size:12px;color:#aaa;padding:21px 30px}
.signup-btn{position:absolute;left:748px;top:164px;width:121px;height:55px}
.copyright{position:absolute;left:748px;top:291px;font-size:13.5px;color:#333}
</style>
</head>
<body>
<header class="block site-header">
  <div class="brand"><span class="brand-dot"></span>Amberfold Vista Group</div>
  <nav class="main-nav"><span>About Us</span><span>Services</span><span>Reviews</span><span>Contact Us</span></nav>
</header>

<section class="block hero" role="img" aria-label="Aerial view of large solar panel field">
  <h1>Innovative Energy Solutions for<br>a Greener Tomorrow!</h1>
  <p>Helping businesses and communities transition to renewable energy with cutting-edge consulting and innovative solutions</p>
  <span class="btn btn-light">Contact Us</span>
</section>

<section class="block vision">Vision: To act as a fiduciary to society and the environment by responsibly utilizing entrusted resources and delivering high-quality consulting services in the energy generation sector, improving people’s quality of life worldwide</section>

<section class="block about">
  <h2>About Us</h2>
  <p>“At Amberfold Vista Group, we empower businesses with innovative renewable energy solutions, helping connect people, power, and planet for a sustainable future.”</p>
  <span class="btn btn-dark">Learn More</span>
  <div class="photo" role="img" aria-label="Wind turbine over misty hills" style="left:468px;top:33px;width:222px;height:358px;background:linear-gradient(180deg,#8d9594,#56605c 60%,#2f3a34)"></div>
  <div class="photo" role="img" aria-label="Solar panels on a house roof" style="left:699px;top:33px;width:222px;height:358px;background:linear-gradient(180deg,#3f7ad6,#253049 55%,#6b6458)"></div>
  <div class="photo" role="img" aria-label="Electric vehicle charging connector" style="left:930px;top:33px;width:222px;height:358px;background:linear-gradient(90deg,#2b4fc8,#3358d8 60%,#e2e5ee)"></div>
</section>

<section class="block services">
  <div class="photo" role="img" aria-label="Solar panels on a blue house roof" style="left:49px;top:18px;width:500px;height:571px;background:linear-gradient(180deg,#3b8be6 0%,#1f2a40 45%,#6c6356 80%,#2b3a55)"></div>
  <h2>Our Services</h2>
  <ol class="service-list">
    <li><strong>Renewable Energy Consulting</strong><em>Expert guidance to help your business adopt clean and sustainable energy solutions, reducing costs and environmental impact.</em></li>
    <li><strong>Solar System Installation</strong><em>Custom-designed solar systems for homes and businesses, ensuring maximum efficiency and long-term energy savings.</em></li>
    <li><strong>Energy Audits</strong><em>In-depth energy assessments to identify opportunities for cost reduction and sustainability improvements.</em></li>
    <li><strong>Battery Storage Solutions</strong><em>Advanced battery storage systems to store and manage renewable energy effectively for uninterrupted power.</em></li>
  </ol>
  <span class="btn btn-light">Explore All Services</span>
</section>

<section class="block stories">
  <h2>“Client Success Stories”</h2>
  <blockquote>"Amberfold Vista Group reduced our energy costs by 40% with a custom solar installation. Their team’s expertise ensured a seamless transition to renewable energy!"</blockquote>
  <cite>— Marcus Hale —</cite>
</section>

<div class="block mosaic" role="img" aria-label="Collage of solar installation project photos" style="top:2052px;background:linear-gradient(90deg,#5d6a78,#8a8a7c 25%,#43506a 50%,#9a8f7a 75%,#4e5c70)"></div>

<section class="block commit">
  <h2>Sustainability Commitment</h2>
  <p>10 million kWh of clean energy generated.</p>
</section>

<div class="block mosaic" role="img" aria-label="Collage of solar farm and rooftop installation photos" style="top:2497px;height:262px;background:linear-gradient(90deg,#4e5c70,#9a8f7a 30%,#5d6a78 55%,#8a8a7c 80%,#43506a)"></div>

<div class="block" style="top:2759px;height:859px">
  <div class="photo" role="img" aria-label="Wind turbines on a forested hillside under grey sky" style="left:0;top:0;width:603px;height:859px;background:linear-gradient(180deg,#a3a9a6,#6f7a74 50%,#2c3a30)"></div>
  <div class="photo" role="img" aria-label="Electric vehicle charging post in a car park" style="left:603px;top:0;width:597px;height:859px;background:linear-gradient(180deg,#3f4f2c,#7a7f74 45%,#5f6260)"></div>
</div>

<footer class="block site-footer">
  <p class="footer-tag">“We empower businesses with innovative renewable energy solutions, connecting people, power, and planet for a sustainable future.”</p>
  <ul class="footer-links"><li>About Us</li><li>Services</li><li>Client Success Stories</li><li>Contact Us</li></ul>
  <div class="social"><span></span><span></span></div>
  <p class="signup-label">Sign up to receive news and updates.</p>
  <div class="email">Email Address</div>
  <span class="btn btn-dark signup-btn">Sign Up</span>
  <p class="copyright">© 2024 Amberfold Vista Group. All Rights Reserved.</p>
</footer>
</body>
</html>
```